Modern, profession Order Insert Card for Head Shop/Smoke shop

We are looking for a modern design for our Order Insert cards where we will have some text thanking the customer for their order.
The design needs to be professional and modern, showing our logo (SVG attached) and our website URL.
Our eCommerce store sells "head shop" items, things like bongs, rolling papers, cbd products, disposable vapes, etc.
I have uploaded 2 versions of our logo, one featuring the colour of green we use across our brand, a black logo or the logo can be inverted to be a white logo on a black background.
Target Market(s)
The websites target audience is anyone needing accessories or tools to consume medicinal marijuana/the consumers favourite herbs or any one in the vaping community.
Contact Information for Business Card
Website URL, Space for a small thank you note and our logo.
Look and feel
Each slider illustrates characteristics of the customer's brand and the style your logo design should communicate.

```html
<!DOCTYPE html>
<html lang="en">
<head>
<meta charset="utf-8">
<title>Leafline Supply – Order Insert Card</title>
<link rel="stylesheet" href="https://fonts.googleapis.com/css2?family=Inter:wght@400;500;800&display=swap">
<style>
  :root {
    --board-green: #536332;
    --card-green: #94c135;
    --ink-white: #ffffff;
    --card-shadow: rgba(30, 40, 15, 0.45);
  }
  * { margin: 0; padding: 0; box-sizing: border-box; }
  html, body {
    width: 1200px;
    height: 1200px;
    overflow: hidden;
    background: var(--board-green);
    font-family: "Inter", Helvetica, Arial, sans-serif;
    color: var(--ink-white);
  }
  .board {
    position: relative;
    width: 1200px;
    height: 1200px;
    background: var(--board-green);
  }
  .insert-card {
    position: absolute;
    width: 514px;
    height: 514px;
    border-radius: 50%;
    background: var(--card-green);
    box-shadow: 0 4px 22px var(--card-shadow);
  }
  .insert-card--front { left: 84px; top: 339px; }
  .insert-card--back { left: 617px; top: 341px; }

  .brand-ring {
    position: absolute;
    inset: 0;
    width: 514px;
    height: 514px;
  }
  .brand-ring text {
    fill: var(--ink-white);
    font-family: "Inter", Helvetica, Arial, sans-serif;
    font-weight: 800;
    font-size: 38px;
  }

  .brand-name {
    position: absolute;
    left: 0;
    right: 0;
    text-align: center;
    font-weight: 800;
    color: var(--ink-white);
    line-height: 1.05;
    letter-spacing: 0.02em;
  }
  .insert-card--front .brand-name {
    top: 205px;
    font-size: 48px;
  }
  .insert-card--back .brand-name {
    top: 78px;
    font-size: 32px;
  }

  .thank-you-note {
    position: absolute;
    left: 40px;
    right: 40px;
    top: 207px;
    text-align: center;
    font-size: 19px;
    font-weight: 400;
    line-height: 23px;
    letter-spacing: 0.16em;
  }
  .website {
    position: absolute;
    left: 0;
    right: 0;
    top: 360px;
    text-align: center;
    font-size: 16px;
    letter-spacing: 0.03em;
  }
  .address {
    position: absolute;
    left: 175px;
    top: 385px;
    font-size: 16px;
    line-height: 19.5px;
    letter-spacing: 0.06em;
    font-style: normal;
  }

  .presentation-note {
    position: absolute;
    left: 132px;
    top: 938px;
    font-size: 31px;
    font-weight: 400;
    line-height: 41px;
    letter-spacing: 0.04em;
  }
  .presentation-note p + p { margin-top: 40px; }
</style>
</head>
<body>
<main class="board">

  <section class="insert-card insert-card--front" aria-label="Insert card front">
    <svg class="brand-ring" viewBox="0 0 514 514" aria-hidden="true">
      <defs>
        <path id="ring-path" d="M257,257 m-210,0 a210,210 0 1,1 420,0 a210,210 0 1,1 -420,0"/>
      </defs>
      <text>
        <textPath href="#ring-path" textLength="1300" lengthAdjust="spacing">LEAFLINE SUPPLY  LEAFLINE SUPPLY  LEAFLINE SUPPLY  LEAFLINE SUPPLY</textPath>
      </text>
    </svg>
    <div class="brand-name">LEAFLINE<br>SUPPLY</div>
  </section>

  <section class="insert-card insert-card--back" aria-label="Insert card back">
    <div class="brand-name">LEAFLINE<br>SUPPLY</div>
    <p class="thank-you-note">We genuinely appreciate your business, and we’re grateful for the trust you’ve placed in us. We hope you are satisfied with your purchase.</p>
    <p class="website">www.leafline-supply.com</p>
    <address class="address">Leafline Supply Ltd,<br>Marlow House 42,<br>Fenwick Lane London,<br>N4 7QT</address>
  </section>

  <div class="presentation-note">
    <p>The business card is designed in a way that<br>allows smokers to clean their green on it.</p>
    <p>Making it a useful asset.</p>
  </div>

</main>
</body>
</html>
```